Health Care Company with Logo Needs Business Cards designed

We are a luxury behavioral health company looking for business cards design we already have a logo and are looking for someone to design a sophisticated luxurious looking business card. Please note that Card design should be captivating just like the logo and also encompass the logo color

Industry/Entity Type

Healthcare

Contact Information for Business Card

Logo,company name, tagline, my name and title, contact details, and physical address

```html
<!DOCTYPE html>
<html lang="en">
<head>
<meta charset="utf-8">
<title>Corvin Behavioral Health – Business Card</title>
<link href="https://fonts.googleapis.com/css2?family=Roboto+Condensed:wght@400;700&family=Roboto:ital,wght@0,400;1,400&display=swap" rel="stylesheet">
<style>
  :root {
    --page-bg: #2b2b2c;
    --card-bg: #2a2a2c;
    --card-bg-dark: #1f1f21;
    --purple: #7b3a8c;
    --blue: #1a8fd0;
    --orange: #e08a1e;
    --green: #8bb534;
    --ink-deep: #0e0e0f;
    --text-light: #e4e4e6;
    --text-soft: #cfcfd2;
  }
  * { margin: 0; padding: 0; box-sizing: border-box; }
  html, body { width: 1200px; height: 1138px; overflow: hidden; }
  body {
    background: var(--page-bg);
    position: relative;
    font-family: "Roboto", Arial, sans-serif;
  }
  .card {
    position: absolute;
    border-radius: 16px;
    overflow: hidden;
    background: linear-gradient(160deg, var(--card-bg) 0%, var(--card-bg-dark) 100%);
    box-shadow: 0 6px 14px rgba(0,0,0,.45);
  }
  /* Front */
  .card-front { left: 274px; top: 186px; width: 624px; height: 376px; }
  .front-name {
    position: absolute; left: 0; right: 0; top: 244px;
    text-align: center;
    font-family: "Roboto Condensed", "Arial Narrow", sans-serif;
    font-weight: 700; font-size: 42px; color: var(--ink-deep);
    letter-spacing: .5px;
  }
  .front-tagline {
    position: absolute; left: 0; right: 0; top: 342px;
    text-align: center;
    font-family: "Roboto Condensed", "Arial Narrow", sans-serif;
    font-weight: 700; font-size: 12.5px; color: var(--text-soft);
    letter-spacing: 3.2px;
  }
  /* Back */
  .card-back { left: 276px; top: 608px; width: 618px; height: 374px; }
  .brand-mark {
    position: absolute; left: 34px; top: 54px; width: 64px; height: 64px;
    background: var(--purple);
  }
  .brand-name {
    position: absolute; left: 143px; top: 52px;
    font-family: "Roboto Condensed", "Arial Narrow", sans-serif;
    font-weight: 700; font-size: 47px; line-height: 1; color: var(--purple);
  }
  .brand-tagline {
    position: absolute; left: 143px; top: 110px;
    font-family: "Roboto Condensed", "Arial Narrow", sans-serif;
    font-weight: 700; font-size: 15.5px; color: var(--blue);
    letter-spacing: 3.1px;
  }
  .person-name {
    position: absolute; left: 30px; top: 218px;
    font-family: "Roboto Condensed", "Arial Narrow", sans-serif;
    font-size: 24px; color: var(--purple);
  }
  .person-title {
    position: absolute; left: 30px; top: 250px;
    font-style: italic; font-size: 15px; color: var(--text-light);
  }
  .address {
    position: absolute; left: 30px; top: 296px;
    font-size: 15px; line-height: 22px; color: var(--text-light); font-style: normal;
  }
  .contact-list {
    position: absolute; left: 318px; top: 216px; list-style: none;
  }
  .contact-list li {
    display: flex; align-items: center; gap: 12px;
    height: 22px; font-size: 15px; color: var(--text-light);
  }
  .contact-list svg { width: 14px; height: 14px; flex: none; }
  .footer-band {
    position: absolute; right: 0; bottom: 0; width: 372px; height: 46px;
  }
  .footer-tagline {
    position: absolute; right: 16px; bottom: 16px;
    font-family: "Roboto Condensed", "Arial Narrow", sans-serif;
    font-weight: 700; font-size: 11.5px; color: var(--text-light);
    letter-spacing: 2.6px;
  }
  .colour-strip {
    position: absolute; left: 0; bottom: 0; height: 8px; display: flex;
  }
  .colour-strip span { display: block; height: 100%; }
  .strip-orange { width: 100px; background: var(--orange); }
  .strip-blue { width: 100px; background: var(--blue); }
  .strip-green { width: 60px; background: var(--green); }
</style>
</head>
<body>

<section class="card card-front" aria-label="Card front">
  <div class="front-name">Corvin Behavioral Health</div>
  <div class="front-tagline">DEDICATED TO HOPE, HEALING AND RECOVERY</div>
</section>

<section class="card card-back" aria-label="Card back">
  <div class="brand-mark"></div>
  <div class="brand-name">Corvin Behavioral Health</div>
  <div class="brand-tagline">DEDICATED TO HOPE, HEALING AND RECOVERY</div>

  <div class="person-name">DANIEL REYES</div>
  <div class="person-title">Managing Director</div>
  <address class="address">123, Anywhere ST, Any City,<br>Any Town, US 123456</address>

  <ul class="contact-list">
    <li>
      <svg viewBox="0 0 14 14" aria-hidden="true"><path d="M2 5 Q7 1 12 5 L10.5 6.5 L9 5 H5 L3.5 6.5 Z M3.5 7 H10.5 L11.5 12 H2.5 Z" fill="var(--purple)"/></svg>
      000-222-0000
    </li>
    <li>
      <svg viewBox="0 0 14 14" aria-hidden="true"><rect x="1" y="3" width="12" height="8" fill="var(--purple)"/><path d="M1 3 L7 8 L13 3" stroke="var(--blue)" stroke-width="1.2" fill="none"/></svg>
      hello@corvinbehavioral.com
    </li>
    <li>
      <svg viewBox="0 0 14 14" aria-hidden="true"><circle cx="7" cy="7" r="5.5" fill="var(--blue)" opacity=".7"/><path d="M1.5 7 H12.5 M7 1.5 V12.5 M7 1.5 Q3.5 7 7 12.5 M7 1.5 Q10.5 7 7 12.5" stroke="var(--purple)" stroke-width=".8" fill="none"/></svg>
      www.corvinbehavioral.com
    </li>
  </ul>

  <svg class="footer-band" viewBox="0 0 372 46" preserveAspectRatio="none" aria-hidden="true">
    <path d="M24 0 H360 Q372 0 372 12 V46 H0 Z" fill="var(--purple)"/>
  </svg>
  <div class="footer-tagline">DEDICATED TO HOPE, HEALING AND RECOVERY</div>

  <div class="colour-strip" aria-hidden="true">
    <span class="strip-orange"></span><span class="strip-blue"></span><span class="strip-green"></span>
  </div>
</section>

</body>
</html>
```